Brochure to promote unique premium vehicle brokerage and detailing service

We are a new business offering a unique way of selling your car privately. We yield our customers higher than trade in and consignment returns on second hand vehicles, positioning each vehicle as best in the market to achieve the optimum outcome. We manage the whole process from start to finish so customers don't have to do any of the administration, negotiating or physical work attached to selling a car.

The problem is no one knows this service exists. We want people to know we are new, honest and worthwhile - they will end up with more in their pocket using our help. We also need to appeal to the 'right' customers. We are looking to attract customers selling cars worth greater than $AUD 50,000 second hand. In all our material we try to convey a luxury, premium feel. We have a website and logo for which we provided similar brief.

There is another side to our business, which is mobile car detailing and paint protection. This is a competitive market and again, we target luxury car owners. Our services are far superior to any bricks and mortar car wash or detailing facility and the average Velmora driver is probably not going to see value in what we offer.

I am not sure whether this brief is for a brochure or a flyer, it is probably something in between? I am envisioning probably 1 A4 sheet folded to create 3 columns, potentially setting out the 2 sides of the business 1 on each side? I am very open to all suggestions/advice. It may make more sense to split the 2 entirely.

We don't want detailed pricing set out as we want to brochure to be valid for a long time. I would prefer a "starting at" for the detailing and paint protection and no specific price on the sales side of things as it is too complex to explain in a brochure.

We have a website which we did our own copywriting for so you could use some of that text. Please let me know in your response if copywriting represents a challenge. Our previous freelancer withdrew because she was unable to write. I am specifically looking for someone who can prepare decent marketing text.

We are Sydney based and available for phone, face to face or email communication. Our website is www.crestmoorautocare.com.au. I have attached a couple of logo files but I do have other formats of the images.

Target Market(s)

These customers are inexperienced or uncomfortable negotiators. They have potentially be putting off buying a vehicle for fear of the process, or are unaware of their negotiating power at a vehicle dealer.

Industry/Entity Type

Marketing

Font styles to use
Other font styles liked:
• Arial is close. Please check our website

Requirements
Must have
• I would like the designer to write the content. Most of this can come from our website. I wrote all of it myself and have it in word format if that is easier to work with.
Nice to have
• We operate 2 service streams - the vehicle brokerage service and a premium detailing service. My biggest priority is targeting vehicle sales/brokerage customers currently. Therefore I am open to dedicating all the energy to that purpose and separately scoping the detailing services if appropriate.
• However, if the flyer could be multi purpose and address both services, maybe one on each side, that may serve me better. The target market for detailing services is vehicle owners of luxury vehicles who are discerning in their preference for perfect presentation of their vehicle, yet do not have the time or ability to achieve this independently.
Should not have
• cartoons,caricatures, gimmicky items that cheapen the feel.

```html
<!DOCTYPE html>
<html lang="en">
<head>
<meta charset="utf-8">
<title>Crestmoor Auto Care – Brochure</title>
<link href="https://fonts.googleapis.com/css2?family=Arimo:wght@400;700&display=swap" rel="stylesheet">
<style>
:root{
  --backdrop:#d6d7d9;
  --panel:#050507;
  --blue:#2ea4ea;
  --white:#ffffff;
  --soft:#d9dde2;
}
*{box-sizing:border-box;margin:0;padding:0}
html,body{width:1200px;height:1000px;overflow:hidden}
body{background:var(--backdrop);font-family:"Arimo",Arial,sans-serif;color:var(--white);position:relative}
.panel{position:absolute;left:280px;width:640px;height:465px;background:var(--panel);overflow:hidden;border:1px solid #222}
.panel--sell{top:20px}
.panel--detail{top:515px}
.main{position:absolute;left:0;top:0;width:430px;height:100%;text-align:center}
.side{position:absolute;right:0;top:0;width:210px;height:100%}
.title{font-size:27px;font-weight:700;letter-spacing:.3px;color:var(--white);margin-top:12px}
.title .accent{color:var(--blue)}
.body{font-size:12.5px;line-height:1.3;color:var(--soft)}
.body b,.hl{color:var(--white);font-weight:700}
.brand-name{color:var(--blue)}
.lead{margin-top:6px}
.gap{height:13px}
.services{list-style:none;font-size:13.5px;line-height:1.32;color:var(--white);margin-top:14px;position:relative;z-index:1}
.car-shade{position:absolute;left:100px;top:335px;width:240px;height:70px;border-radius:50%;
  background:radial-gradient(ellipse at center,#2c2f35 0%,#15171b 55%,rgba(5,5,7,0) 75%)}
.call{position:absolute;left:100px;top:385px;text-align:left}
.call-label{font-size:15px;color:var(--white);margin-left:4px}
.call-number{display:flex;align-items:center;gap:8px;font-size:29px;color:var(--white);margin-top:2px}
.brand{position:absolute;top:82px;right:8px;display:flex;align-items:center;justify-content:flex-end;gap:6px}
.brand-mark{width:10px;height:10px;background:var(--blue)}
.brand-text{font-size:14px;font-weight:400;color:var(--blue)}
.vertical{position:absolute;left:4px;bottom:22px;writing-mode:vertical-rl;transform:rotate(180deg);
  font-size:18px;font-weight:700;letter-spacing:2px;white-space:nowrap;line-height:22px}
.vertical .accent{color:var(--blue)}
.pattern{position:absolute;right:0;bottom:0;width:210px;height:250px;
  background:radial-gradient(circle at 70% 75%,#2a2d33 0%,#17191d 45%,rgba(5,5,7,0) 75%)}
.quote{position:absolute;right:10px;bottom:14px;text-align:right;font-size:11px;line-height:1.3;color:var(--white);white-space:nowrap}
.quote cite{display:block;font-style:normal;color:var(--blue)}
/* detailing */
.tagline{font-size:11.5px;line-height:1.22;color:var(--white);margin-top:3px}
.intro{font-size:9.5px;line-height:1.25;color:var(--soft);margin-top:4px;padding:0 8px}
.compare{display:flex;justify-content:center;gap:50px;margin-top:5px}
.shot{width:120px}
.shot-label{font-size:11px;color:var(--blue);text-align:left;padding-left:6px}
.shot-photo{height:60px;border:1px solid #777}
.shot-photo--before{background:linear-gradient(160deg,#e6e7e9 0%,#b9bcc1 55%,#3b3d42 100%)}
.shot-photo--after{background:linear-gradient(170deg,#c9dcee 0%,#8fa8c2 50%,#2e3642 100%)}
.columns{display:flex;justify-content:center;gap:14px;margin-top:7px}
.col{width:200px}
.col-head{font-size:10px;font-weight:700;color:var(--blue);margin-bottom:4px}
.col ul{list-style:none;font-size:8.5px;line-height:1.22;color:var(--white)}
.col small{font-size:6.5px;display:block;line-height:1.1;color:var(--soft)}
.price{font-size:8.5px;color:var(--white);margin-top:6px}
</style>
</head>
<body>

<section class="panel panel--sell" aria-label="Sell your car">
  <div class="main">
    <h1 class="title"><span class="accent">SELL</span> YOUR CAR</h1>
    <p class="body lead">Are you time poor?<br>Are you uncomfortable with strangers coming to your house?<br>Are you unhappy with trade in prices?</p>
    <div class="gap"></div>
    <p class="body">At <span class="brand-name hl">Crestmoor Auto Care</span> we remove the time,<br>uncomfortable interactions and stress from the process.<br>Servicing Sydney's eastern suburbs,<br>we'll sit down and review the market<br>with you to establish a price and guide you through.<br>We aim to yield the <b>highest possible</b><br><b>sale</b> price by making your car <b>stand out</b> from the crowd.</p>
    <div class="car-shade" role="img" aria-label="Dark front view of a luxury car"></div>
    <ul class="services">
      <li>• Detailing</li>
      <li>• Photography</li>
      <li>• Price advice</li>
      <li>• Listing of ad</li>
      <li>• Show vehicle to potential buyers</li>
      <li>• Vet buyers</li>
      <li>• Negotiate sale price and broker sale</li>
    </ul>
    <div class="call">
      <div class="call-label">Call Now</div>
      <div class="call-number">
        <svg width="16" height="22" viewBox="0 0 16 22" aria-hidden="true"><path d="M4 1 L7 6 L5 8 Q6 13 9 16 L11 14 L15 18 L12 21 Q2 18 1 4 Z" fill="#2ea4ea"/></svg>
        <span>0400 555 018</span>
      </div>
    </div>
  </div>
  <div class="side">
    <div class="pattern" role="img" aria-label="Faint decorative line pattern"></div>
    <div class="brand"><span class="brand-mark"></span><span class="brand-text">Crestmoor Auto Care</span></div>
    <div class="vertical"><span class="accent">SELL</span> YOUR CAR</div>
    <p class="quote">Wow, it looks better than new!<cite>Mark, Kingsford</cite></p>
  </div>
</section>

<section class="panel panel--detail" aria-label="Car detailing services">
  <div class="main">
    <h1 class="title"><span class="accent">CAR DETAILING</span> SERVICES</h1>
    <p class="tagline">Quality detailing using the industry's best products and<br>methods from an award winning operator</p>
    <p class="intro"><span class="brand-name hl">CAC</span> is for the motoring enthusiast who demands more. We use the best <b>professional</b> products and the <b>best</b> methods to ensure your vehicle is in better condition than others. Your absolute <b>satisfaction</b> is our priority.<br>We come to you. Whether it's a one off and some pointers for maintaining it, or a weekly appointment on your driveway to keep your car in peak condition, let us show you the <span class="brand-name hl">CAC</span> difference.<br>Our offering is simple and our service <b>quality</b> – there isn't a billboard of extras to chose from, just a promise of our best work on every job.</p>
    <div class="compare">
      <figure class="shot"><figcaption class="shot-label">Before</figcaption><div class="shot-photo shot-photo--before" role="img" aria-label="Silver car bonnet before detailing"></div></figure>
      <figure class="shot"><figcaption class="shot-label">After</figcaption><div class="shot-photo shot-photo--after" role="img" aria-label="Polished car bonnet reflecting the sky after detailing"></div></figure>
    </div>
    <div class="columns">
      <div class="col">
        <h2 class="col-head">Standard Wash Package</h2>
        <ul>
          <li>Full exterior clean using 2 bucket method<small>(always with fresh mitts and towels)</small></li>
          <li>Interior vacuum and trim clean</li>
          <li>Windows<small>(interior and exterior)</small></li>
          <li>Door jambs</li>
          <li>Tyre shine</li>
          <li>Small mark removal</li>
          <li>Spray wax</li>
          <li>Wheel arch clean</li>
        </ul>
        <p class="price">Less than 4 weeks since last CAC service: $60</p>
        <p class="price">More than 4 weeks since last CAC service: $80</p>
        <p class="price">SUVs attract a $10 surcharge.</p>
      </div>
      <div class="col">
        <h2 class="col-head">Detailing Services</h2>
        <ul>
          <li>• Paint and interior assessment</li>
          <li>• Stage 1,2 or 3 machine polish</li>
          <li>• Leather or fabric clean and treat</li>
          <li>• Engine bay detail</li>
          <li>• Full exterior clean using 2 bucket method</li>
          <li>• Interior vacuum and trim clean</li>
          <li>• Windows (interior and exterior)</li>
          <li>• Door jambs</li>
          <li>• Tyre shine</li>
          <li>• Small mark removal</li>
          <li>• Spray wax</li>
          <li>• Wheel arch clean</li>
        </ul>
        <p class="price">POA – starting at $300</p>
      </div>
    </div>
  </div>
  <div class="side">
    <div class="pattern" role="img" aria-label="Faint decorative line pattern"></div>
    <div class="brand"><span class="brand-mark"></span><span class="brand-text">Crestmoor Auto Care</span></div>
    <div class="vertical"><span class="accent">CAR DETAILING</span> SERVICES</div>
    <p class="quote">Thank you for all your advice,<br>I feel so much more comfortable<br>with my purchase thanks to<br>your help.<cite>Claire, Sydney</cite></p>
  </div>
</section>

</body>
</html>
```